high-impact, conversion-focused website redesign for the government sector

Objective: To design and develop a high-impact, conversion-focused digital platform that solidifies Harrowgate Lumen Advisors (HLA) as the leading communications and strategy firm for government, defense, and industrial clients. The site must project authority, innovation, and sophisticated precision. See the creative breif for more information

Target Market(s)

Government contractors

Industry/Entity Type

Government, defense, industrials

Coding

Coded - Design and coding required

Number of Pages Required

5+ page

Font styles to use
Other font styles liked:
• See the current website

Requirements
Must have
• See design brief
Nice to have
• See design brief
Should not have
• See design brief

```html
<!DOCTYPE html>
<html lang="en">
<head>
<meta charset="utf-8">
<title>Harrowgate Lumen Advisors — Accelerate Your Mission</title>
<link rel="stylesheet" href="https://fonts.googleapis.com/css2?family=Lexend+Exa:wght@400;500&family=Lexend:wght@300;400;500;600;700&display=swap">
<style>
:root{
  --navy:#13294d;
  --navy-deep:#0c1f3d;
  --blue:#1d86f0;
  --green:#7dc22b;
  --green-dark:#5aa82a;
  --orange:#f7941d;
  --ink:#1b2a44;
  --text:#4a5468;
  --muted:#8a93a3;
  --line:#e3e8ef;
  --panel:#f2f4f7;
  --white:#ffffff;
}
*{box-sizing:border-box;margin:0;padding:0}
html,body{width:1200px;height:4134px;overflow:hidden}
body{position:relative;background:var(--white);font-family:"Lexend",sans-serif;color:var(--text)}
.abs{position:absolute}
.display{font-family:"Lexend Exa",sans-serif;font-weight:500;color:var(--ink);letter-spacing:.5px}
.btn{position:absolute;display:flex;align-items:center;justify-content:center;font-family:"Lexend",sans-serif;font-weight:600;font-size:11px;color:#fff;background:var(--blue);clip-path:polygon(8% 0,92% 0,100% 50%,92% 100%,8% 100%,0 50%);letter-spacing:.3px}

/* nav */
.site-nav{position:absolute;left:0;top:0;width:1200px;height:64px;background:#fff}
.site-nav a{position:absolute;top:27px;font-size:11px;color:var(--navy);text-decoration:none;transform:translateX(-50%);white-space:nowrap}
.brand{position:absolute;display:flex;align-items:center;gap:6px;font-family:"Lexend",sans-serif;font-weight:500;white-space:nowrap}
.brand i{display:block;background:var(--orange)}

/* hero */
.hero{position:absolute;left:0;top:64px;width:1200px;height:620px;background:linear-gradient(180deg,#3d5f86 0%,#6c8fb5 35%,#4d6f97 60%,#2f4a6e 100%)}
.hero-title{position:absolute;left:0;top:172px;width:1200px;text-align:center;font-family:"Lexend Exa",sans-serif;font-weight:400;font-size:46px;color:#fff;letter-spacing:1px}
.hero-sub{position:absolute;left:0;top:236px;width:1200px;text-align:center;font-size:11.5px;color:#fff;font-weight:500}
.hero-shapes{position:absolute;left:0;top:440px}
.btn.ghost{background:transparent;clip-path:none;outline:1.5px solid #fff}

/* stats */
.stat{position:absolute;top:578px;width:313px;height:160px;background:#fff;box-shadow:0 4px 16px rgba(20,40,80,.12);text-align:center}
.stat b{display:block;margin-top:26px;font-family:"Lexend Exa",sans-serif;font-weight:500;font-size:42px;color:var(--ink)}
.stat p{margin:10px auto 0;width:210px;font-size:10px;line-height:1.45;color:var(--text)}

/* services */
.section-title{position:absolute;left:0;width:1200px;text-align:center;font-size:25px}
.service{position:absolute;width:229px;height:153px;background:#fff;border:1px solid var(--line);box-shadow:0 2px 8px rgba(20,40,80,.06);overflow:hidden}
.service .icon{position:absolute;left:24px;top:20px;width:58px;height:50px;background:#e6f2d6;clip-path:polygon(25% 0,75% 0,100% 50%,75% 100%,25% 100%,0 50%)}
.service h3{position:absolute;left:24px;bottom:14px;font-size:14px;font-weight:600;color:var(--ink);line-height:1.2}
.service .corner{position:absolute;right:0;bottom:0}

/* who we are */
.who-photo{position:absolute;left:112px;top:1241px;width:488px;height:383px;background:linear-gradient(160deg,#5b7f9f 0%,#3f6a5a 55%,#1d3a3a 100%)}
.who-panel{position:absolute;left:600px;top:1241px;width:488px;height:383px;background:var(--panel)}
.who-panel h2{position:absolute;left:53px;top:62px;font-size:25px}
.who-panel p{position:absolute;left:53px;top:104px;width:405px;font-size:10.5px;line-height:1.65}
.bullets{position:absolute;left:53px;top:224px;display:grid;grid-template-columns:205px 200px;row-gap:12px;font-size:10.5px;font-weight:600;color:var(--ink)}
.bullets span{display:flex;align-items:center;gap:7px}
.bullets span::before{content:"";width:9px;height:9px;border-radius:50%;background:linear-gradient(90deg,var(--orange) 50%,var(--blue) 50%)}

/* testimonials */
.testimonials{position:absolute;left:0;top:1640px;width:1200px;height:492px;background:var(--navy);clip-path:polygon(0 0,100% 30px,100% 100%,0 100%)}
.testimonials h2{position:absolute;left:0;top:120px;width:1200px;text-align:center;color:#fff;font-size:25px}
.quote{position:absolute;top:174px;width:313px;height:246px;background:#fff;text-align:center}
.quote.featured{border:3px solid var(--green)}
.quote .avatar{width:56px;height:56px;border-radius:50%;background:#cdd4de;margin:22px auto 0}
.quote .stars{margin-top:10px;color:#f5b400;font-size:13px;letter-spacing:2px}
.quote p{width:268px;margin:10px auto 0;font-size:9.5px;line-height:1.9;color:var(--text)}
.quote h4{margin-top:12px;font-size:11px;font-weight:600;color:var(--ink)}
.quote small{display:block;font-size:9.5px;color:var(--muted)}
.dots{position:absolute;left:0;top:446px;width:1200px;display:flex;justify-content:center;gap:5px}
.dots i{width:7px;height:7px;border-radius:50%;background:#fff}
.dots i.on{background:var(--green)}

/* edge */
.edge{position:absolute;left:0;top:2131px;width:1200px;height:413px;background:var(--panel)}
.edge h2{position:absolute;left:112px;top:108px;font-size:25px}
.edge p{position:absolute;left:112px;width:405px;font-size:10.5px;line-height:1.7}
.edge-photo{position:absolute;left:607px;top:63px;width:481px;height:294px;background:linear-gradient(180deg,#4f7fb8 0%,#9cc0e4 55%,#8f9aa6 75%,#5f6a74 100%)}

/* expect */
.wheel{position:absolute;left:110px;top:2612px;width:420px;height:420px;border-radius:50%;background:linear-gradient(90deg,#7dc22b 0%,#9fcf4e 50%,#f7941d 100%)}
.expect h2{position:absolute;left:571px;top:2636px;font-size:25px;line-height:1.25}
.expect p{position:absolute;left:571px;width:490px;font-size:10.5px;line-height:1.75}
.expect em{font-style:normal;color:var(--orange)}

/* banner */
.banner{position:absolute;left:112px;top:3107px;width:976px;height:154px;background:linear-gradient(90deg,#16345f 0%,#1c3d6b 60%,#2a4d7a 100%)}
.banner h2{position:absolute;left:58px;top:45px;color:#fff;font-size:25px;line-height:1.25}
.field{position:absolute;top:43px;width:175px;height:28px;background:#fff;font-size:9.5px;color:#a0a8b5;display:flex;align-items:center;padding-left:18px;clip-path:polygon(6% 0,94% 0,100% 50%,94% 100%,6% 100%,0 50%)}
.banner .btn{top:88px;left:548px;width:366px;height:30px}

/* news */
.post{position:absolute;top:3377px;width:313px;height:315px;background:#fff;box-shadow:0 3px 12px rgba(20,40,80,.1)}
.post .thumb{position:absolute;left:14px;top:0;width:285px;height:178px}
.post .date{position:absolute;left:14px;top:196px;display:flex;align-items:center;gap:6px;font-size:10px;color:var(--text)}
.post h3{position:absolute;left:14px;top:218px;font-size:14px;font-weight:600;color:var(--ink)}
.post p{position:absolute;left:14px;top:243px;width:285px;font-size:9.5px;line-height:1.5}
.post a{position:absolute;left:14px;top:278px;font-size:10px;font-weight:500;color:var(--blue);text-decoration:none}

/* footer */
.footer{position:absolute;left:0;top:3808px;width:1200px;height:326px;background:var(--navy)}
.footer h4{position:absolute;top:44px;font-size:13px;font-weight:700;color:#fff;letter-spacing:.3px}
.footer ul{position:absolute;top:76px;list-style:none;font-size:10.5px;color:#d9e1ec;line-height:21px}
.footer .about{position:absolute;left:112px;top:112px;width:240px;font-size:9.5px;line-height:1.75;color:#d9e1ec}
.badge{position:absolute;top:192px;height:34px;background:#e8ecf1}
.contact{position:absolute;left:908px;top:76px;font-size:10.5px;line-height:19px;color:#fff}
.footer hr{position:absolute;left:112px;top:288px;width:976px;border:0;border-top:1px solid rgba(255,255,255,.25)}
.footer .copy{position:absolute;left:0;top:300px;width:1200px;text-align:center;font-size:10px;color:#d9e1ec}
</style>
</head>
<body>

<nav class="site-nav">
  <a href="#" style="left:290px">ADVISORY SERVICES</a>
  <a href="#" style="left:438px">ABOUT US</a>
  <div class="brand" style="left:490px;top:24px;font-size:12px;color:var(--navy)"><i style="width:10px;height:10px"></i>Harrowgate Lumen Advisors</div>
  <a href="#" style="left:747px">BLOG</a>
  <a href="#" style="left:855px">CONTACT</a>
</nav>

<header class="hero" role="img" aria-label="Wide photo of an industrial aerospace manufacturing hall with steel roof trusses, tinted blue">
  <h1 class="hero-title">ACCELERATE YOUR MISSION</h1>
  <p class="hero-sub">We empower federal-focused organizations with the strategy, communications, and connections needed to advance mission-critical outcomes</p>
  <div class="btn" style="left:438px;top:293px;width:122px;height:28px">GET IN TOUCH</div>
  <div class="btn ghost" style="left:576px;top:293px;width:184px;height:28px">EXPLORE OUR SERVICES</div>
  <svg class="hero-shapes" width="1200" height="180" viewBox="0 0 1200 180" aria-hidden="true">
    <polygon points="0,110 112,180 0,180" fill="var(--orange)"/>
    <polygon points="0,100 420,180 1200,10 1200,180 0,180" fill="#fff"/>
    <polygon points="1200,40 1200,180 1080,180" fill="var(--green)"/>
  </svg>
</header>

<div class="stat" style="left:112px"><b>72%</b><p>increase in database contacts through CRM implementation and targeted marketing campaigns</p></div>
<div class="stat" style="left:444px"><b>100+</b><p>introductions to tech-scouting contracts across the DoD and the aerospace &amp; defense ecosystem</p></div>
<div class="stat" style="left:775px"><b>570%</b><p>Positioned a client for transformative growth, fueling increase in stock price and attracting $50M AUD in new investment</p></div>

<h2 class="display section-title" style="top:792px">OUR SERVICES</h2>

<div class="service" style="left:112px;top:852px"><div class="icon" role="img" aria-label="Network of people icon"></div><h3>Corporate<br>Communication</h3>
  <svg class="corner" width="52" height="52"><polygon points="52,0 52,52 0,52" fill="var(--blue)"/><path d="M27 40h15m-4-4 4 4-4 4" stroke="#fff" stroke-width="1.6" fill="none"/></svg></div>
<div class="service" style="left:361px;top:852px"><div class="icon" role="img" aria-label="Handshake icon"></div><h3>Public Relation</h3>
  <svg class="corner" width="52" height="52"><polygon points="52,0 52,52 0,52" fill="var(--blue)"/><path d="M27 40h15m-4-4 4 4-4 4" stroke="#fff" stroke-width="1.6" fill="none"/></svg></div>
<div class="service" style="left:610px;top:852px"><div class="icon" role="img" aria-label="Government building icon"></div><h3>Government<br>Affairs</h3>
  <svg class="corner" width="52" height="52"><polygon points="52,0 52,52 0,52" fill="var(--blue)"/><path d="M27 40h15m-4-4 4 4-4 4" stroke="#fff" stroke-width="1.6" fill="none"/></svg></div>
<div class="service" style="left:858px;top:852px"><div class="icon" role="img" aria-label="Team alert icon"></div><h3>Crisis<br>Communications</h3>
  <svg class="corner" width="52" height="52"><polygon points="52,0 52,52 0,52" fill="var(--blue)"/><path d="M27 40h15m-4-4 4 4-4 4" stroke="#fff" stroke-width="1.6" fill="none"/></svg></div>

<div class="service" style="left:112px;top:1024px"><div class="icon" role="img" aria-label="Digital dashboard icon"></div><h3>Digital<br>Marketing</h3>
  <svg class="corner" width="52" height="52"><polygon points="52,0 52,52 0,52" fill="var(--blue)"/><path d="M27 40h15m-4-4 4 4-4 4" stroke="#fff" stroke-width="1.6" fill="none"/></svg></div>
<div class="service" style="left:361px;top:1024px"><div class="icon" role="img" aria-label="Connected team icon"></div><h3>Strategic<br>Connections</h3>
  <svg class="corner" width="52" height="52"><polygon points="52,0 52,52 0,52" fill="var(--blue)"/><path d="M27 40h15m-4-4 4 4-4 4" stroke="#fff" stroke-width="1.6" fill="none"/></svg></div>
<div class="service" style="left:610px;top:1024px"><div class="icon" role="img" aria-label="Investment hand icon"></div><h3>Investor<br>Relations</h3>
  <svg class="corner" width="52" height="52"><polygon points="52,0 52,52 0,52" fill="var(--blue)"/><path d="M27 40h15m-4-4 4 4-4 4" stroke="#fff" stroke-width="1.6" fill="none"/></svg></div>
<div class="service" style="left:858px;top:1024px"><div class="icon" role="img" aria-label="Calendar icon"></div><h3>Event<br>Management</h3>
  <svg class="corner" width="52" height="52"><polygon points="52,0 52,52 0,52" fill="var(--blue)"/><path d="M27 40h15m-4-4 4 4-4 4" stroke="#fff" stroke-width="1.6" fill="none"/></svg></div>

<div class="who-photo" role="img" aria-label="Photo of an air traffic control tower interior with green-lit consoles overlooking a runway at dusk"></div>
<section class="who-panel">
  <h2 class="display">WHO WE ARE</h2>
  <p>Harrowgate Lumen Advisors is a strategic communications firm built for government, defense, and industrial leaders who operate in complex, mission-critical environments. We translate technical challenges into clear narratives, actionable strategies, and measurable impact. Our team brings decades of experience supporting high-stakes programs where precision, alignment, and execution aren't optional—they're essential.</p>
  <div class="bullets">
    <span>Federal &amp; defense experts</span><span>High-stakes comms specialists</span>
    <span>Mission-focused strategists</span><span>Trusted advisors to innovators</span>
  </div>
  <div class="btn" style="left:53px;top:290px;width:120px;height:28px">LEARN MORE</div>
</section>

<section class="testimonials">
  <h2 class="display">TESTIMONIALS</h2>
  <div class="quote" style="left:112px"><div class="avatar" role="img" aria-label="Client portrait"></div><div class="stars">★★★★★</div>
    <p>HLA understands the mission, the environment, and the stakes. Their strategic insight and ability to communicate with precision helped us strengthen key relationships and advance critical priorities</p><h4>Calvin R.</h4><small>General</small></div>
  <div class="quote featured" style="left:444px"><div class="avatar" role="img" aria-label="Client portrait" style="margin-top:19px"></div><div class="stars">★★★★★</div>
    <p>Working with Harrowgate Lumen made a measurable impact on our event strategy and execution. Their network, organization, and ability to secure high-caliber speakers elevated our entire program</p><h4>Nora P.</h4><small>General</small></div>
  <div class="quote" style="left:775px"><div class="avatar" role="img" aria-label="Client portrait"></div><div class="stars">★★★★★</div>
    <p>The HLA team operates with the professionalism and precision you expect from top-tier defense partners. Their ability to navigate both policy and communications challenges set them apart</p><h4>Martin Okafor</h4><small>General</small></div>
  <div class="dots"><i></i><i class="on"></i><i></i><i></i><i></i><i></i></div>
</section>

<section class="edge">
  <h2 class="display">OUR EDGE</h2>
  <p style="top:150px">We combine deep federal sector insight, technical understanding, and a powerful network across government, industry, investors, and media. Our proven approach drives results — from major contract wins and successful M&amp;A to increased valuation, strategic investment, and political support.</p>
  <p style="top:226px">Our strategies begin with your mission and business goals, ensuring every message, relationship, and action advances growth and impact.</p>
  <div class="btn" style="left:112px;top:284px;width:120px;height:28px">LEARN MORE</div>
  <div class="edge-photo" role="img" aria-label="Photo of a vintage four-engine bomber aircraft parked on a tarmac under a cloudy sky"></div>
</section>

<div class="wheel" role="img" aria-label="Circular infographic of services in green and orange segments surrounding the brand at its centre"></div>

<section class="expect">
  <h2 class="display">WHAT TO EXPECT WHEN<br>PARTNERING WITH US</h2>
  <p style="top:2712px">With <em>decades of experience</em>, a results-focused methodology, and cutting-edge marketing and communications tools and technologies, we begin every engagement with a discovery and planning process to ensure we are building a strategy that cuts through the noise to achieve our measurable results. <em>As specialists in government crisis communications</em>, we additionally examine our client's current strategy for risks ensuring we are building on a stable foundation.</p>
  <p style="top:2812px">By truly understanding our client's goals, key milestones, potential areas of risk, ideal customer and investor targets, partner profiles, and other key drivers, <em>we create messaging and strategy that goes beyond traditional brand awareness</em> to meet mission objectives. As a full service firm, we work across all the areas in the graphic.</p>
  <p style="top:2893px">Our <em>time-tested methodology</em> is based on building and executing a strategy aligned with client mission objectives. With the strategy in place, we execute tactics with precision, efficiency, and the highest quality of customer service.</p>
  <div class="btn" style="left:571px;top:2971px;width:124px;height:28px">GET IN TOUCH</div>
</section>

<section class="banner" aria-label="Contact banner">
  <h2 class="display">ADVANCE YOUR MISSION<br>WITH PRECISION</h2>
  <div class="field" style="left:548px">Enter Name</div>
  <div class="field" style="left:739px">Enter Email</div>
  <div class="btn">SEND</div>
</section>

<h2 class="display section-title" style="top:3318px">OUR LATEST NEWS &amp; BLOG</h2>

<article class="post" style="left:112px">
  <div class="thumb" role="img" aria-label="Photo of a jet engine on an assembly stand in a workshop" style="background:linear-gradient(160deg,#3a4d66,#8a6a4a 60%,#2b3442)"></div>
  <div class="date"><svg width="11" height="11" viewBox="0 0 11 11"><rect x=".5" y="1.5" width="10" height="9" fill="none" stroke="#4a5468"/><path d="M.5 4h10" stroke="#4a5468"/></svg>June 15, 2025</div>
  <h3>Insights &amp; Analysis</h3>
  <p>Expert updates on defense, government, and technology—clear, concise, and mission-focused</p>
  <a href="#">Learn More ⟶</a>
</article>
<article class="post" style="left:444px">
  <div class="thumb" role="img" aria-label="Photo of an aircraft in a teal-lit operations hangar with screens" style="background:linear-gradient(160deg,#1d5a6e,#3aa3b5 55%,#14333f)"></div>
  <div class="date"><svg width="11" height="11" viewBox="0 0 11 11"><rect x=".5" y="1.5" width="10" height="9" fill="none" stroke="#4a5468"/><path d="M.5 4h10" stroke="#4a5468"/></svg>June 20, 2025</div>
  <h3>Federal Insights</h3>
  <p>Brief, strategic perspectives on the trends shaping today's national security landscape</p>
  <a href="#">Learn More ⟶</a>
</article>
<article class="post" style="left:775px">
  <div class="thumb" role="img" aria-label="Photo of industrial storage silos under a blue sky" style="background:linear-gradient(180deg,#6f9fd6,#b9c6d2 55%,#7d8791)"></div>
  <div class="date"><svg width="11" height="11" viewBox="0 0 11 11"><rect x=".5" y="1.5" width="10" height="9" fill="none" stroke="#4a5468"/><path d="M.5 4h10" stroke="#4a5468"/></svg>June 25, 2025</div>
  <h3>Mission-Focused Updates</h3>
  <p>Short, impactful insights to help leaders navigate the federal ecosystem with confidence</p>
  <a href="#">Learn More ⟶</a>
</article>

<div class="btn" style="left:550px;top:3722px;width:100px;height:30px">VIEW ALL</div>

<footer class="footer">
  <div class="brand" style="left:112px;top:66px;font-size:13px;color:#fff"><i style="width:12px;height:12px"></i>Harrowgate Lumen Advisors</div>
  <p class="about">Harrowgate Lumen Advisors delivers strategic communications, government affairs, and marketing solutions that help federal-focused organizations accelerate mission success</p>
  <div class="badge" style="left:112px;width:34px"></div>
  <div class="badge" style="left:150px;width:34px;border-radius:50%"></div>
  <div class="badge" style="left:188px;width:34px"></div>
  <div class="badge" style="left:226px;width:22px"></div>

  <h4 style="left:395px">QUICK LINKS</h4>
  <ul style="left:395px"><li>Home</li><li>Advisory Services</li><li>About Us</li><li>Latest Blog</li><li>Contact Us</li></ul>

  <h4 style="left:620px">OUR SERVICES</h4>
  <ul style="left:620px"><li>Corporate Communication</li><li>Public Relations</li><li>Government Affairs</li><li>Crisis Communications</li><li>Digital Marketing</li><li>Strategic Connections</li><li>Investor Relations</li><li>Event Management</li></ul>

  <h4 style="left:881px">CONTACT US</h4>
  <svg class="abs" style="left:881px;top:76px" width="14" height="18" viewBox="0 0 14 18"><path d="M7 17s6-6.2 6-10A6 6 0 0 0 1 7c0 3.8 6 10 6 10z" fill="none" stroke="var(--green)" stroke-width="1.5"/><circle cx="7" cy="7" r="2" fill="none" stroke="var(--green)" stroke-width="1.5"/></svg>
  <div class="contact"><b>Riverbend Hub</b><br><b>Harrowgate Lumen Advisors</b><br>418 Larkspur Ave<br>Suite 220<br>Denton TX, 76201</div>
  <svg class="abs" style="left:881px;top:194px" width="16" height="11" viewBox="0 0 16 11"><rect x=".75" y=".75" width="14.5" height="9.5" fill="none" stroke="var(--green)" stroke-width="1.5"/><path d="M1 1l7 5 7-5" fill="none" stroke="var(--green)" stroke-width="1.5"/></svg>
  <div class="contact" style="top:190px">info@harrowgatelumen.example</div>

  <hr>
  <p class="copy">©HARROWGATE LUMEN -2025 All rights reserved</p>
</footer>

</body>
</html>
```